Presentation Folder Design - (Pocket Folder)

We are an accounting firm for dentists. We need a folder designed for our marketing material. Attached is our logo.

Accounting

```html
<!DOCTYPE html>
<html lang="en">
<head>
<meta charset="utf-8">
<title>ClearBite Ledger – Pocket Folder</title>
<link rel="stylesheet" href="https://fonts.googleapis.com/css2?family=Open+Sans:wght@300;400&family=Roboto:wght@400;700&display=swap">
<style>
  :root {
    --bg: #f4f4f5;
    --paper: #e9e9eb;
    --paper-light: #f3f3f4;
    --charcoal: #48494c;
    --brand-blue: #1e8ec8;
    --pocket-blue: #1f7fb0;
    --ink: #5a5a5e;
    --sheet: #ffffff;
  }
  * { box-sizing: border-box; margin: 0; padding: 0; }
  html, body { width: 1200px; height: 750px; overflow: hidden; }
  body {
    background: var(--bg);
    position: relative;
    font-family: "Roboto", Arial, sans-serif;
  }
  .brand-name {
    font-family: "Roboto", Arial, sans-serif;
    font-weight: 700;
    color: var(--brand-blue);
    line-height: 1.05;
  }
  .brand-corner { position: absolute; left: 34px; top: 30px; font-size: 30px; }
  .brand-corner small { display: block; font-size: 13px; }
  .board-title {
    position: absolute; left: 46px; top: 180px;
    font-family: "Open Sans", Arial, sans-serif; font-weight: 300;
    font-size: 34px; line-height: 1.1; color: var(--charcoal);
  }
  .panel {
    position: absolute;
    background: linear-gradient(160deg, var(--paper-light), var(--paper));
    box-shadow: 0 6px 18px rgba(0,0,0,.12);
    overflow: hidden;
  }
  .panel svg.bands { position: absolute; left: 0; top: 0; }
  .front-cover { left: 150px; top: 330px; width: 300px; height: 380px; }
  .front-cover .brand-name {
    position: absolute; left: 0; right: 0; top: 180px;
    text-align: center; font-size: 30px;
  }
  .front-cover .brand-name small { display: block; font-size: 12px; }
  .inside-left { left: 560px; top: 110px; width: 300px; height: 440px; }
  .inside-left .brand-name { position: absolute; left: 22px; bottom: 26px; font-size: 22px; }
  .inside-left .brand-name small { display: block; font-size: 9px; }
  .inside-right { left: 860px; top: 110px; width: 300px; height: 440px; }
  .letter {
    position: absolute; left: 32px; top: 26px; width: 236px; height: 330px;
    background: var(--sheet); box-shadow: 0 2px 6px rgba(0,0,0,.15);
    padding: 16px 18px; color: var(--ink);
  }
  .letter .brand-name { font-size: 15px; }
  .letter .brand-name small { display: block; font-size: 7px; }
  .letter .salutation { margin-top: 34px; font-size: 9px; }
  .letter p { margin-top: 10px; font-size: 6px; line-height: 1.55; }
  .pocket {
    position: absolute; left: 0; right: 0; bottom: 0; height: 170px;
    background: var(--pocket-blue);
    box-shadow: 0 -3px 8px rgba(0,0,0,.15);
  }
</style>
</head>
<body>
  <div class="brand-name brand-corner">ClearBite Ledger<small>CPA's Ltd.</small></div>
  <h1 class="board-title">Pocket Folder<br>Packaging Design</h1>

  <section class="panel front-cover">
    <svg class="bands" width="300" height="380" viewBox="0 0 300 380">
      <polygon points="70,0 300,0 300,85" fill="var(--charcoal)"/>
      <polygon points="70,0 300,85 300,125 20,0" fill="var(--brand-blue)"/>
    </svg>
    <div class="brand-name">ClearBite Ledger<small>CPA's Ltd.</small></div>
  </section>

  <section class="panel inside-left">
    <svg class="bands" width="300" height="440" viewBox="0 0 300 440">
      <polygon points="0,0 80,0 0,210" fill="var(--charcoal)"/>
      <polygon points="80,0 115,0 0,290 0,210" fill="var(--brand-blue)"/>
    </svg>
    <div class="brand-name">ClearBite Ledger<small>CPA's Ltd.</small></div>
  </section>

  <section class="panel inside-right">
    <article class="letter">
      <div class="brand-name">ClearBite Ledger<small>CPA's Ltd.</small></div>
      <div class="salutation">Dear Mr. Harlan</div>
      <p>Thank you for choosing our firm to manage your practice books. We look forward to helping your clinic grow with clear monthly reports.</p>
      <p>Enclosed you will find our service guide, fee schedule and a checklist of the documents we need to begin.</p>
      <p>Please call us with any questions about payroll, tax planning or equipment financing for your dental office.</p>
    </article>
    <div class="pocket"></div>
  </section>
</body>
</html>
```